Creative, Modern and Conversion based Web Design

Kovel Digital has recently launched a new logo and as part of our companies rebranding, we need a new website aimed towards the UK B2B marketplace.

The website needs to deliver a modern and creative website design whilst ensuring the design is tailored towards conversion optimisation.

This site must drive point of contact either from an online form, via a direct telephone call or Skype connection.

Our sales are all offline so the website will be a simple, elegant and stunning information portal.

Kovel Digital offers Digital Marketing services to companies throughout the UK - our target audiences are companies that turnover a minimum of 3 million pounds a year and as such we need to deliver a professional image that installs confidence in our companies abilities.

We do not like websites that are reliant upon stock photography - we are happy for stock photography to be used in a small way however the site must not look like a template filled with stock photography.

What do we do

We supply digital marketing services to those companies who demand a strong return on investment - our company prides itself on delivering successful campaigns that help establish long-term profitable relationships.

A lot of the information presented on our old site is relevant today however the design sucks. So please use the information on our current website as a foundation for your design content.

I am looking for several page designs including

"Home Page" Desktop Version
"Service Page" Desktop Version
"Blog Page" Desktop Version

"Home Page" Mobile Version
"Service Page" Mobile Version
"Blog Page" Mobile Version

In the 1st instance please only submit a single design for the "Home Page" Desktop Version - those designers that we are impressed with will be asked to complete the other designs before a winner is selected.

I like modern clean fonts - the site needs to welcome the reader and encourage them to absorb the information - not to overload and make them leave.

The site must be designed to naturally fit our companies new logo.

NO TEMPLATES

Target Market(s)

B2b - 3 million turnover and above

Industry/Entity Type

Digital Marketing

Number of Pages Required

3 page

Requirements
Must have
• Blended well with the companies logo
• We need conversion optimisation to be a huge part of the design - we considered a conversation when a potential customer reaches out to use via - web form, telephone or skype
• The current content on the old website fits today's business but the design sucks.
• www.koveldigital-studio.net
Nice to have
• We need 3 pages (in 2 variants Desktop and Mobile)
• Home Page
• Service Page
• Blog Page
• Please only deliver the "Home Page" desktop version - if we are happy with your design we will aks for the additional pages
Should not have
• No templates and not stock photo heavy design

```html
<!DOCTYPE html>
<html lang="en">
<head>
<meta charset="utf-8">
<title>Kovel Digital – Search Marketing That Actually Delivers</title>
<link href="https://fonts.googleapis.com/css2?family=Jost:wght@400;500;600;700&display=swap" rel="stylesheet">
<style>
:root{
  --blue:#3b6fae;
  --blue-deep:#1f4f94;
  --navy:#1d2733;
  --text:#5f6670;
  --muted:#8a929c;
  --line:#d9dee5;
  --pale:#eef2f8;
  --card:#f6f8fb;
  --footer:#3c434e;
  --white:#ffffff;
}
*{box-sizing:border-box;margin:0;padding:0}
html,body{width:1200px;height:4215px;overflow:hidden}
body{position:relative;background:var(--white);font-family:"Jost",sans-serif;color:var(--text)}
.abs{position:absolute}
a{color:inherit;text-decoration:none}

/* header */
.brand{display:flex;align-items:center;gap:12px;color:var(--white);font-weight:600;font-size:26px;letter-spacing:.5px}
.brand-mark{width:22px;height:22px;background:var(--white)}
.nav{top:56px;left:380px;display:flex;gap:0;font-size:15px;color:var(--navy)}
.nav a{position:absolute;white-space:nowrap}
.nav .active{color:var(--blue)}
.phone-btn{left:900px;top:48px;width:200px;height:39px;border:1.5px solid var(--blue);border-radius:20px;display:flex;align-items:center;justify-content:center;gap:8px;font-size:15px;color:var(--navy)}

/* common */
.eyebrow{display:flex;align-items:center;gap:14px;font-size:14px;color:var(--navy)}
.eyebrow::before{content:"";width:60px;height:2px;background:var(--blue)}
.h-title{color:var(--navy);font-weight:600;line-height:1.18}
.body-text{font-size:14px;line-height:1.55;color:var(--text)}
.btn-solid{background:var(--blue-deep);color:var(--white);border-radius:20px;display:flex;align-items:center;justify-content:center;font-size:14px;box-shadow:0 6px 14px rgba(31,79,148,.3)}
.btn-ghost{border:1.5px solid var(--blue);color:var(--blue-deep);border-radius:20px;display:flex;align-items:center;justify-content:center;font-size:14px;background:var(--white)}
.photo{border-radius:2px}

/* services */
.service-card{background:var(--white);box-shadow:0 8px 28px rgba(29,39,51,.12);text-align:center;padding:50px 34px 0}
.service-card h3{font-weight:500;font-size:21px;color:var(--navy);margin:18px 0 14px}
.service-card p{font-size:13.5px;line-height:1.55}
.read-more{display:inline-block;margin-top:22px;font-size:13px;color:var(--navy);border-bottom:1px solid var(--navy)}
.slider-arrow{color:var(--blue);font-size:20px}

/* partners */
.partner-cell{display:flex;align-items:center;justify-content:center}
.partner-badge{width:150px;height:34px;background:#c9ced6;border-radius:4px}

/* stats */
.stats-band{left:183px;top:2523px;width:1017px;height:371px;background:var(--blue);border-radius:186px 0 0 186px}
.stat{width:200px;text-align:center;color:var(--white)}
.stat-ring{width:96px;height:96px;border-radius:50%;background:var(--white);margin:0 auto 18px;display:flex;align-items:center;justify-content:center}
.stat-num{font-size:22px;font-weight:500}
.stat-label{font-size:19px}

/* blog */
.post-card{background:var(--card);width:324px;height:393px}
.post-card .photo{height:182px}
.post-card h4{font-weight:500;font-size:21px;line-height:1.18;color:var(--navy);margin:22px 22px 14px}
.post-card p{font-size:13.5px;line-height:1.5;margin:0 22px}
.post-card time{display:block;font-size:13px;color:var(--navy);margin:22px 22px 0}
.round-arrow{width:34px;height:34px;border-radius:50%;display:flex;align-items:center;justify-content:center;font-size:16px}

/* contact */
.contact-panel{left:0;top:3445px;width:1113px;height:377px;background:var(--blue)}
.field{color:var(--white);font-size:14px;border-bottom:1px solid rgba(255,255,255,.55);padding-bottom:10px}
.send-btn{border:1.5px solid var(--white);color:var(--white);border-radius:20px;display:flex;align-items:center;justify-content:center;font-size:14px}

/* footer */
.footer{left:0;top:3633px;width:1200px;height:582px;background:var(--footer)}
.footer h5{font-weight:500;font-size:20px;color:var(--white);margin-bottom:20px}
.footer li{list-style:none;font-size:14px;color:#d7dbe1;line-height:2.05}
.footer-contact{color:#d7dbe1;font-size:13.5px;line-height:1.55}
.footer-contact strong{display:block;color:var(--white);font-weight:600;font-size:22px;margin-bottom:6px}
.to-top{width:34px;height:34px;border-radius:50%;background:var(--blue);display:flex;align-items:center;justify-content:center}
.copyright{font-size:13px;color:#c3c8cf;text-align:center}
</style>
</head>
<body>

<!-- background shapes -->
<svg class="abs" style="left:0;top:0" width="1200" height="1900" aria-hidden="true">
  <path d="M0 0H580C500 70 520 240 610 330C680 400 640 560 470 590C320 615 130 570 0 520Z" fill="#3b6fae"/>
  <path d="M470 820C620 760 840 800 1000 900C1120 975 1200 1050 1200 1150V1820H380C300 1700 290 1500 330 1300C360 1100 380 880 470 820Z" fill="#eef2f8"/>
</svg>

<!-- header -->
<header>
  <a class="abs brand" style="left:87px;top:48px" href="#"><span class="brand-mark"></span>Kovel Digital</a>
  <nav class="abs nav" aria-label="Main">
    <a class="active" style="left:0">Home</a>
    <a style="left:84px">About Us</a>
    <a style="left:196px">Services</a>
    <a style="left:303px">Blog</a>
    <a style="left:378px">Contact Us</a>
  </nav>
  <a class="abs phone-btn" href="#">
    <svg width="14" height="14" viewBox="0 0 24 24" aria-hidden="true"><path d="M6.6 10.8a15 15 0 0 0 6.6 6.6l2.2-2.2a1 1 0 0 1 1-.25 11.4 11.4 0 0 0 3.6.57 1 1 0 0 1 1 1V20a1 1 0 0 1-1 1A17 17 0 0 1 3 4a1 1 0 0 1 1-1h3.5a1 1 0 0 1 1 1c0 1.25.2 2.45.57 3.6a1 1 0 0 1-.25 1Z" fill="#3b6fae"/></svg>
    +44 (0) 1632 960418
  </a>
</header>

<!-- hero -->
<section>
  <div class="abs photo" role="img" aria-label="Desktop monitor showing a digital marketing concept board with coloured pencils, keyboard and mouse" style="left:84px;top:183px;width:548px;height:393px;background:linear-gradient(160deg,#f4f5f7 0%,#dfe3e8 55%,#c8cdd4 100%);border-radius:6px"></div>
  <h1 class="abs h-title" style="left:613px;top:262px;font-size:33px;width:420px">Search Marketing That Actually Delivers</h1>
  <p class="abs body-text" style="left:613px;top:360px;width:390px">Search Marketing is our forte, our clients results highlight just how good we do it.</p>
  <a class="abs btn-solid" style="left:613px;top:427px;width:146px;height:38px">Explore Now!</a>
</section>

<!-- about -->
<section>
  <div class="abs eyebrow" style="left:87px;top:728px">About Us</div>
  <h2 class="abs h-title" style="left:87px;top:760px;font-size:33px;width:480px">Do you want to see an enviable ROI on search marketing? It’s possible – you’ve found us.</h2>
  <p class="abs body-text" style="left:87px;top:936px;width:470px;font-size:13.5px">We know and understand the world of business.<br>We know that ROI is the single most important metric in the marketing world. We’ve worked within some of the world’s largest industries – such as finance, insurance, payday loans and health, where achieving above 100% ROI is often impossible …</p>
  <a class="abs btn-solid" style="left:87px;top:1066px;width:146px;height:38px">Contact Us</a>
  <div class="abs photo" role="img" aria-label="Two colleagues reviewing a rising bar chart on a large screen in a meeting room" style="left:613px;top:708px;width:497px;height:410px;background:linear-gradient(135deg,#d7dce2 0%,#b7c0ca 50%,#8d99a6 100%)"></div>
</section>

<!-- services -->
<section>
  <p class="abs" style="left:0;top:1192px;width:1200px;text-align:center;font-size:14px;color:var(--navy)">What We Do</p>
  <h2 class="abs h-title" style="left:0;top:1218px;width:1200px;text-align:center;font-size:30px">Our Services</h2>

  <span class="abs slider-arrow" style="left:48px;top:1444px">‹</span>
  <span class="abs slider-arrow" style="left:1138px;top:1444px">›</span>

  <article class="abs service-card" style="left:87px;top:1293px;width:323px;height:331px">
    <svg width="58" height="58" viewBox="0 0 58 58" fill="none" stroke="#6a7280" stroke-width="2" aria-hidden="true"><circle cx="24" cy="24" r="14"/><path d="M34 34l14 14"/><path d="M17 27l5-5 4 4 7-8"/></svg>
    <h3>Organic Search</h3>
    <p>Attract traffic that converts and interacts with your brand through Organic. We implement both …</p>
    <a class="read-more">Read More</a>
  </article>
  <article class="abs service-card" style="left:438px;top:1293px;width:324px;height:331px">
    <svg width="58" height="58" viewBox="0 0 58 58" fill="none" stroke="#3b6fae" stroke-width="2" aria-hidden="true"><rect x="8" y="18" width="42" height="30" rx="2"/><path d="M8 20l21 16 21-16"/><path d="M20 16V8h18v8"/></svg>
    <h3>Email Marketing</h3>
    <p>Our targeted email marketing campaigns allow you to segment users and deliver custom-tailored …</p>
    <a class="read-more">Read More</a>
  </article>
  <article class="abs service-card" style="left:790px;top:1293px;width:323px;height:331px">
    <svg width="58" height="58" viewBox="0 0 58 58" fill="none" stroke="#6a7280" stroke-width="2" aria-hidden="true"><rect x="8" y="8" width="16" height="16"/><rect x="34" y="8" width="16" height="16"/><rect x="8" y="34" width="16" height="16"/><rect x="34" y="34" width="16" height="16"/><circle cx="29" cy="29" r="5"/></svg>
    <h3>Social Media</h3>
    <p>Your followers are your most loyal customers. Let us develop a comprehensive strategy …</p>
    <a class="read-more">Read More</a>
  </article>

  <a class="abs btn-solid" style="left:537px;top:1664px;width:126px;height:36px">View All</a>
</section>

<!-- link placements -->
<section>
  <div class="abs photo" role="img" aria-label="Hands typing on a keyboard at a desk with a colourful SEO illustration on screen, glasses and coffee" style="left:87px;top:1776px;width:498px;height:410px;background:linear-gradient(135deg,#e9a17e 0%,#9fb7c9 55%,#5f6f7d 100%)"></div>
  <div class="abs eyebrow" style="left:641px;top:1790px">Handle SEO Yourself? Perfect.</div>
  <h2 class="abs h-title" style="left:641px;top:1822px;font-size:31px;width:470px">Hassle-Free Link Placements That Drive Rankings</h2>
  <p class="abs body-text" style="left:641px;top:1920px;width:470px;font-size:13.5px">Our link placements are used by some of the world’s largest companies in the most difficult industries – such as payday loans, insurance, finance, health and legal. We use our link placement service in conjunction with our Organic Search (SEO) offerings; although some of our clients handle their SEO in-house and prefer to use our link placements to bolster their rankings.</p>
  <p class="abs" style="left:641px;top:2078px;font-size:13.5px;font-weight:600;color:var(--navy)">Here’s how our unique, link acquisition process works …</p>
  <a class="abs btn-ghost" style="left:641px;top:2134px;width:126px;height:36px">Read More</a>
</section>

<!-- partners -->
<section aria-label="Tools and partners">
  <svg class="abs" style="left:87px;top:2248px" width="1026" height="216" aria-hidden="true">
    <line x1="342" y1="0" x2="342" y2="216" stroke="#d9dee5"/>
    <line x1="684" y1="0" x2="684" y2="216" stroke="#d9dee5"/>
    <line x1="0" y1="112" x2="1026" y2="112" stroke="#d9dee5"/>
  </svg>
  <div class="abs partner-cell" style="left:87px;top:2248px;width:342px;height:112px"><span class="partner-badge"></span></div>
  <div class="abs partner-cell" style="left:429px;top:2248px;width:342px;height:112px"><span class="partner-badge"></span></div>
  <div class="abs partner-cell" style="left:771px;top:2248px;width:342px;height:112px"><span class="partner-badge"></span></div>
  <div class="abs partner-cell" style="left:87px;top:2360px;width:342px;height:104px"><span class="partner-badge"></span></div>
  <div class="abs partner-cell" style="left:429px;top:2360px;width:342px;height:104px"><span class="partner-badge"></span></div>
  <div class="abs partner-cell" style="left:771px;top:2360px;width:342px;height:104px"><span class="partner-badge"></span></div>
</section>

<!-- stats -->
<section>
  <div class="abs stats-band"></div>
  <h2 class="abs" style="left:183px;top:2578px;width:1017px;text-align:center;color:var(--white);font-weight:600;font-size:31px;line-height:1.25">We Grow as Our Clients Grow.<br>That’s What We Love.</h2>
  <div class="abs stat" style="left:369px;top:2678px">
    <div class="stat-ring"><svg width="36" height="36" viewBox="0 0 36 36" fill="none" stroke="#3b6fae" stroke-width="2.2" aria-hidden="true"><circle cx="13" cy="13" r="5"/><circle cx="24" cy="13" r="5"/><path d="M3 30c0-6 5-9 10-9s10 3 10 9M18 22c2-1 4-1 6-1 5 0 9 3 9 9"/></svg></div>
    <div class="stat-num">117</div><div class="stat-label">Satisfied Clients</div>
  </div>
  <div class="abs stat" style="left:631px;top:2678px">
    <div class="stat-ring"><svg width="34" height="34" viewBox="0 0 34 34" fill="none" stroke="#3b6fae" stroke-width="2.2" aria-hidden="true"><rect x="4" y="4" width="26" height="26" rx="2"/><path d="M10 17l5 5 9-10"/></svg></div>
    <div class="stat-num">215</div><div class="stat-label">Campaigns Finished</div>
  </div>
  <div class="abs stat" style="left:889px;top:2678px">
    <div class="stat-ring"><svg width="34" height="34" viewBox="0 0 34 34" fill="none" stroke="#3b6fae" stroke-width="2.2" aria-hidden="true"><path d="M6 10h18v14a6 6 0 0 1-6 6h-6a6 6 0 0 1-6-6Z"/><path d="M24 13h3a4 4 0 0 1 0 8h-3"/><path d="M11 4v3M16 4v3"/></svg></div>
    <div class="stat-num">1,798</div><div class="stat-label">Cups of Coffee</div>
  </div>
</section>

<!-- blog -->
<section>
  <div class="abs eyebrow" style="left:87px;top:2976px">Blog</div>
  <h2 class="abs h-title" style="left:87px;top:3008px;font-size:30px;width:320px">Check What Happening Inside Kovel Digital Ltd</h2>
  <p class="abs body-text" style="left:87px;top:3142px;width:300px;font-size:13.5px">Our link placements are used by some of the world’s largest companies in the most difficult industries.</p>
  <span class="abs round-arrow" style="left:87px;top:3251px;border:1.5px solid var(--blue);color:var(--blue)">←</span>
  <span class="abs round-arrow" style="left:131px;top:3251px;background:var(--blue-deep);color:var(--white)">→</span>
  <a class="abs btn-ghost" style="left:87px;top:3333px;width:130px;height:36px">View All</a>

  <article class="abs post-card" style="left:438px;top:2979px">
    <div class="photo" role="img" aria-label="Laptop on a desk displaying analytics charts" style="background:linear-gradient(135deg,#7b8a99 0%,#c9b59a 60%,#5c4a3a 100%)"></div>
    <h4>Contrary to popular belief, classical latin</h4>
    <p>But I must explain to you how all this mistaken idea of denouncing pleasure and praising pain …</p>
    <time>01-Sep-2018</time>
  </article>
  <article class="abs post-card" style="left:790px;top:2979px">
    <div class="photo" role="img" aria-label="Hands typing on a laptop keyboard" style="background:linear-gradient(135deg,#d3d6da 0%,#9aa1a9 55%,#4d545c 100%)"></div>
    <h4>Contrary to popular belief, classical latin</h4>
    <p>But I must explain to you how all this mistaken idea of denouncing pleasure and praising pain …</p>
    <time>01-Sep-2018</time>
  </article>
</section>

<!-- footer background -->
<div class="abs footer"></div>

<!-- contact -->
<section>
  <div class="abs contact-panel"></div>
  <div class="abs eyebrow" style="left:87px;top:3514px;color:var(--white)">Have a Projects?</div>
  <h2 class="abs" style="left:87px;top:3554px;color:var(--white);font-weight:600;font-size:31px;line-height:1.2">Get in touch<br>with us.</h2>
  <form>
    <div class="abs field" style="left:438px;top:3516px;width:284px">Your Name:</div>
    <div class="abs field" style="left:742px;top:3516px;width:284px">Business Name:</div>
    <div class="abs field" style="left:438px;top:3576px;width:284px">Phone:</div>
    <div class="abs field" style="left:742px;top:3576px;width:284px">Email:</div>
    <div class="abs field" style="left:438px;top:3644px;width:588px">Your Message:</div>
    <div class="abs send-btn" style="left:438px;top:3709px;width:112px;height:37px">Send</div>
  </form>
</section>

<!-- footer content -->
<footer>
  <div class="abs brand" style="left:87px;top:3900px;font-size:24px"><span class="brand-mark"></span>Kovel Digital</div>
  <div class="abs footer-contact" style="left:87px;top:3994px;width:300px">
    <strong>Call: 01632 960418</strong>
    Email: hello@koveldigital-studio.net<br><br>
    Kovel Digital Ltd The Granary 12 Elmfield Rd Northwick Hill Ashbury AB1 2CD
  </div>
  <div class="abs" style="left:464px;top:3890px">
    <h5>Locations We Cover</h5>
    <ul><li>Birmingham</li><li>London</li><li>Manchester</li><li>Stoke-on-Trent</li><li style="color:var(--white)">→ See All Locations</li></ul>
  </div>
  <div class="abs" style="left:759px;top:3890px">
    <h5>Our Key Services</h5>
    <ul><li>Link Outreach</li><li>Organic Search (SEO)</li><li>Paid Search (PPC)</li><li>Social Media Marketing</li></ul>
  </div>
  <a class="abs to-top" style="left:1076px;top:3897px" aria-label="Back to top">
    <svg width="14" height="14" viewBox="0 0 14 14" aria-hidden="true"><path d="M7 12V2M2 7l5-5 5 5" stroke="#fff" stroke-width="2" fill="none"/></svg>
  </a>
  <div class="abs" style="left:87px;top:4145px;width:1026px;height:1px;background:rgba(255,255,255,.18)"></div>
  <p class="abs copyright" style="left:0;top:4170px;width:1200px">© 2018 Kovel Digital Limited. All rights reserved.</p>
</footer>

</body>
</html>
```